Northfield Heritage Construction & Affiliates Redesigning our Look

We need stationary (letterhead, envelopes, notepads, invoicing templates, etc) that all coordinate. We are an commerial and residential exteriors construction company that operates 3 companies which all run exclusively, however, the compliment one another well.

Northfield Heritage Construction (this company installs exteriors on jobsites both residential and commercial)
Northfield Heritage Roofing & Building Supply (this company sells exterior building materials to homeowners and builders.)
Northfield Heritage Dumpster Services (This company delivers roll away dumpster cans to homeowners and builders)

Just a note: When I say we do exterior work. We do roofing, siding, stone, windows/doors, gutters, and decks.

We are looking for stationary that includes all three and keeps with our patriotic theme

Info on our firm:
Address: 2719 Tamsworth Rd, Bailey MI 49317
Phone: 231-555-0187
Website: www.northfieldheritage.example

Target Market(s)

Our companies target market is vast. We work in the B2B space as well as with homeowner (retail customers). We are in the home and commercial buiding construction field. We specialized in exteriors. (Roofing, Siding, Stone, Windows, Doors, Decks, Gutters)

Industry/Entity Type

Construction

Colors
ec1f27
ffffff
0555a3

Requirements
Must have
• Would like to have a clean professional look with a patriotic theme
Nice to have
• Red/White/Blue

```html
<!DOCTYPE html>
<html lang="en">
<head>
<meta charset="utf-8">
<title>Northfield Heritage Stationery</title>
<link rel="stylesheet" href="https://fonts.googleapis.com/css2?family=Playfair+Display:wght@600&family=Source+Sans+3:wght@400;600&display=swap">
<style>
  :root{
    --bg:#e4e6e6;
    --paper:#ffffff;
    --ink:#222222;
    --red:#ef4a40;
    --blue:#0555a3;
    --muted:#6b6b6b;
    --muted-dark:#bdbdbd;
    --silhouette-dark:#3a2320;
    --silhouette-light:#f8d3cf;
    --disc-hub:#d9dcdc;
  }
  *{margin:0;padding:0;box-sizing:border-box}
  html,body{width:1200px;height:900px;overflow:hidden}
  body{background:var(--bg);position:relative;font-family:"Source Sans 3",sans-serif}
  .piece{position:absolute;overflow:hidden;box-shadow:0 6px 18px rgba(0,0,0,.18)}
  .piece--light{background:var(--paper)}
  .piece--dark{background:var(--ink)}
  .band{position:absolute;left:0;width:100%}
  .band path{fill:var(--red)}
  .band .band__rule{fill:var(--blue)}
  .silhouette{position:absolute}
  .piece--light .silhouette{background:var(--silhouette-light)}
  .piece--dark .silhouette{background:var(--silhouette-dark)}

  .brand{position:absolute;display:flex;align-items:flex-end;gap:.3em;font-family:"Playfair Display",serif;font-weight:600;line-height:.95;letter-spacing:-.02em;white-space:nowrap}
  .brand__name{display:flex;flex-direction:column}
  .piece--light .brand{color:var(--ink)}
  .piece--dark .brand{color:var(--paper)}
  .brand__mark{width:.6em;height:.6em;background:var(--blue);flex:none;margin-bottom:.12em}

  .contact{position:absolute;font-size:10px;line-height:1.35;white-space:nowrap}
  .piece--light .contact{color:var(--muted)}
  .piece--dark .contact{color:var(--muted-dark)}
  .contact strong{font-weight:600;color:var(--blue)}
  .piece--dark .contact strong{color:var(--paper)}
  .contact--right{text-align:right}
  .affiliates{position:absolute;display:flex;gap:14px;font-size:9px;font-weight:600;white-space:nowrap;color:var(--ink)}
  .affiliates li{list-style:none;display:flex;align-items:center;gap:4px}
  .affiliates li::before{content:"";width:5px;height:5px;background:var(--red);flex:none}
  .footer-rule{position:absolute;left:14px;right:14px;height:2px;background:var(--blue)}

  .envelope{left:40px;top:40px;width:460px;height:230px}
  .envelope__flap{position:absolute;left:0;top:0;width:100%;height:44px;background:var(--ink)}
  .card-dark{left:40px;top:310px;width:210px;height:120px}
  .card-light{left:280px;top:310px;width:210px;height:120px}
  .notepad{left:40px;top:470px;width:460px;height:300px}
  .folder{left:540px;top:40px;width:300px;height:420px}
  .letterhead{left:860px;top:40px;width:300px;height:388px}
  .sleeve{left:540px;top:500px;width:300px;height:300px}
  .disc{left:860px;top:500px;width:300px;height:300px;border-radius:50%}
  .disc__hub{position:absolute;left:115px;top:115px;width:70px;height:70px;border-radius:50%;background:var(--disc-hub)}
  .disc__hole{position:absolute;left:137px;top:137px;width:26px;height:26px;border-radius:50%;background:var(--bg)}
</style>
</head>
<body>

<section class="piece piece--light envelope">
  <div class="envelope__flap"></div>
  <div class="brand" style="left:16px;top:54px;font-size:20px"><span class="brand__name"><span>Northfield</span><span>Heritage</span></span><span class="brand__mark"></span></div>
  <svg class="band" style="top:98px;height:100px" viewBox="0 0 100 100" preserveAspectRatio="none"><path d="M0 0H38L34 12L100 60V90L62 62L0 35Z"/><path class="band__rule" d="M0 40L62 67L100 95V98L62 70L0 43Z"/></svg>
  <div class="silhouette" style="left:400px;top:156px;width:50px;height:30px" role="img" aria-label="Soldier silhouette illustration"></div>
  <p class="contact" style="left:16px;bottom:12px">2719 Tamsworth Rd, Bailey MI 49317 · <strong>231-555-0187</strong></p>
</section>

<section class="piece piece--dark card-dark">
  <p class="contact contact--right" style="right:10px;top:10px;font-size:8px"><strong>231-555-0187</strong><br>www.northfieldheritage.example</p>
  <div class="brand" style="left:10px;top:38px;font-size:11px"><span class="brand__name"><span>Northfield</span><span>Heritage</span></span><span class="brand__mark"></span></div>
  <svg class="band" style="top:66px;height:40px" viewBox="0 0 100 100" preserveAspectRatio="none"><path d="M0 0H38L34 15L100 60V95L62 62L0 40Z"/></svg>
  <div class="silhouette" style="left:150px;top:80px;width:36px;height:30px" role="img" aria-label="Tank silhouette illustration"></div>
</section>

<section class="piece piece--light card-light">
  <p class="contact contact--right" style="right:10px;top:10px;font-size:8px">2719 Tamsworth Rd, Bailey MI 49317<br><strong>231-555-0187</strong> · www.northfieldheritage.example</p>
  <div class="brand" style="left:10px;top:38px;font-size:11px"><span class="brand__name"><span>Northfield</span><span>Heritage</span></span><span class="brand__mark"></span></div>
  <svg class="band" style="top:66px;height:40px" viewBox="0 0 100 100" preserveAspectRatio="none"><path d="M0 0H38L34 15L100 60V95L62 62L0 40Z"/></svg>
  <div class="silhouette" style="left:168px;top:88px;width:26px;height:16px" role="img" aria-label="Soldier silhouette illustration"></div>
</section>

<section class="piece piece--light notepad">
  <div class="brand" style="left:18px;top:16px;font-size:26px"><span class="brand__name"><span>Northfield</span><span>Heritage</span></span><span class="brand__mark"></span></div>
  <svg class="band" style="top:70px;height:110px" viewBox="0 0 100 100" preserveAspectRatio="none"><path d="M0 0H40L36 12L100 58V92L62 62L0 34Z"/><path class="band__rule" d="M0 39L62 67L100 96V99L62 70L0 42Z"/></svg>
  <div class="silhouette" style="left:395px;top:134px;width:52px;height:38px" role="img" aria-label="Soldier silhouette illustration"></div>
  <div class="footer-rule" style="bottom:40px"></div>
  <p class="contact" style="left:14px;bottom:16px">2719 Tamsworth Rd, Bailey MI 49317 · <strong>231-555-0187</strong> · www.northfieldheritage.example</p>
</section>

<section class="piece piece--dark folder">
  <div class="brand" style="left:14px;top:14px;font-size:20px"><span class="brand__name"><span>Northfield</span><span>Heritage</span></span><span class="brand__mark"></span></div>
  <svg class="band" style="top:60px;height:60px" viewBox="0 0 100 100" preserveAspectRatio="none"><path d="M0 0H45L40 15L100 45V90L60 62L0 45Z"/></svg>
  <p class="contact" style="left:14px;bottom:14px">2719 Tamsworth Rd, Bailey MI 49317<br><strong>231-555-0187</strong> · www.northfieldheritage.example</p>
</section>

<section class="piece piece--light letterhead">
  <div class="brand" style="left:14px;top:14px;font-size:20px"><span class="brand__name"><span>Northfield</span><span>Heritage</span></span><span class="brand__mark"></span></div>
  <svg class="band" style="top:60px;height:80px" viewBox="0 0 100 100" preserveAspectRatio="none"><path d="M0 0H42L38 12L100 58V92L62 62L0 34Z"/><path class="band__rule" d="M0 39L62 67L100 96V99L62 70L0 42Z"/></svg>
  <div class="silhouette" style="left:250px;top:108px;width:40px;height:28px" role="img" aria-label="Soldier silhouette illustration"></div>
  <div class="footer-rule" style="bottom:58px"></div>
  <ul class="affiliates" style="left:14px;bottom:38px;flex-direction:column;gap:2px;display:none"></ul>
  <p class="contact" style="left:14px;bottom:10px;font-size:8px;line-height:1.4">Construction · Roofing &amp; Building Supply · Dumpster Services<br>2719 Tamsworth Rd, Bailey MI 49317 · <strong>231-555-0187</strong> · www.northfieldheritage.example</p>
  <ul class="affiliates" style="left:14px;bottom:66px;flex-direction:column;gap:3px;font-size:8px">
    <li>Northfield Heritage Construction</li>
    <li>Northfield Heritage Roofing &amp; Building Supply</li>
    <li>Northfield Heritage Dumpster Services</li>
  </ul>
</section>

<section class="piece piece--dark sleeve">
  <div class="brand" style="left:14px;top:166px;font-size:18px"><span class="brand__name"><span>Northfield</span><span>Heritage</span></span><span class="brand__mark"></span></div>
  <svg class="band" style="top:212px;height:80px" viewBox="0 0 100 100" preserveAspectRatio="none"><path d="M0 0H40L36 12L100 58V100L62 64L0 36Z"/></svg>
  <div class="silhouette" style="left:220px;top:252px;width:44px;height:36px" role="img" aria-label="Tank silhouette illustration"></div>
  <p class="contact contact--right" style="right:14px;top:14px"><strong>231-555-0187</strong><br>www.northfieldheritage.example</p>
</section>

<section class="piece piece--light disc">
  <div class="disc__hub"></div>
  <div class="disc__hole"></div>
  <div class="brand" style="left:26px;top:168px;font-size:13px"><span class="brand__name"><span>Northfield</span><span>Heritage</span></span><span class="brand__mark"></span></div>
  <svg class="band" style="top:200px;height:66px" viewBox="0 0 100 100" preserveAspectRatio="none"><path d="M0 0H40L36 12L100 58V96L62 62L0 34Z"/></svg>
  <div class="silhouette" style="left:240px;top:238px;width:30px;height:22px" role="img" aria-label="Soldier silhouette illustration"></div>
  <p class="contact" style="left:0;right:0;bottom:20px;text-align:center;font-size:8px">www.northfieldheritage.example</p>
</section>

</body>
</html>
```